Design for Certificate

Design a certificate for training, providing our company logo such as attachments. Company's name is "BRYNE Fjellvik Advisory Ltd", please refer to our company profile: https://www.bryne-fjellvik.example/company_info

The style of the current certificate is also attached, and another certificate of another company can be referred to. Psd & jpg are required for the final draft (the layers of psd are not merged). Thanks!

```html
<!DOCTYPE html>
<html lang="en">
<head>
<meta charset="utf-8">
<title>Certificate of Completion – BRYNE Fjellvik Advisory Ltd</title>
<link href="https://fonts.googleapis.com/css2?family=Josefin+Sans:wght@600;700&family=Playfair+Display:wght@400&display=swap" rel="stylesheet">
<style>
  :root {
    --bg: #564a40;
    --bg-light: #6b5a4a;
    --gold: #d8ad4c;
    --gold-soft: #c99a3e;
    --cream: #efe6d8;
    --rule: #d9d2c8;
  }
  * { margin: 0; padding: 0; box-sizing: border-box; }
  html, body { width: 1200px; height: 848px; overflow: hidden; background: var(--bg); }
  .certificate {
    position: relative;
    width: 1200px;
    height: 848px;
    overflow: hidden;
    background: linear-gradient(160deg, #544840 0%, var(--bg) 55%, var(--bg-light) 100%);
  }
  .certificate__art { position: absolute; inset: 0; }
  .line { position: absolute; left: 0; width: 1200px; text-align: center; }
  .display {
    font-family: "Josefin Sans", sans-serif;
    font-weight: 700;
    color: var(--gold);
    text-transform: uppercase;
    line-height: 1;
  }
  .caption {
    font-family: "Playfair Display", serif;
    color: var(--cream);
    text-transform: uppercase;
    letter-spacing: 0.3em;
    font-size: 15px;
    line-height: 1;
  }
  .title { top: 52px; font-size: 76px; letter-spacing: 0.02em; }
  .subtitle { top: 117px; font-size: 45px; color: var(--gold-soft); }
  .awarded { top: 216px; }
  .recipient { top: 252px; font-size: 64px; letter-spacing: 0.02em; }
  .completed { top: 376px; }
  .course { top: 408px; font-size: 42px; color: var(--gold-soft); line-height: 39px; }
  .session { top: 503px; font-size: 17px; }
  .session__date {
    font-family: "Josefin Sans", sans-serif;
    font-weight: 600;
    color: var(--gold);
    letter-spacing: 0;
    font-size: 22px;
    margin-left: 6px;
  }
  .cert-number { position: absolute; top: 724px; left: 197px; width: 257px; text-align: center; }
  .signatory {
    position: absolute; top: 724px; left: 757px; width: 258px; text-align: center;
    line-height: 20px;
  }
  .signature {
    position: absolute; left: 760px; top: 642px; width: 250px; height: 58px;
    background: linear-gradient(90deg, rgba(239,230,216,0.05), rgba(239,230,216,0.16), rgba(239,230,216,0.05));
    border-radius: 4px;
  }
  .company {
    position: absolute; top: 787px; left: 440px; width: 320px; text-align: center;
    font-size: 20px; letter-spacing: 0.25em;
  }
</style>
</head>
<body>
<main class="certificate">
  <svg class="certificate__art" width="1200" height="848" viewBox="0 0 1200 848" aria-hidden="true">
    <defs>
      <g id="corner-ornament" fill="none" stroke="var(--gold)" stroke-width="1.2">
        <rect x="40" y="31" width="56" height="56"/>
        <line x1="96" y1="31" x2="96" y2="149"/>
        <line x1="40" y1="87" x2="159" y2="87"/>
        <path d="M96 145 l3 4 -3 4 -3 -4z M155 87 l4 -3 4 3 -4 3z" fill="var(--gold)" stroke="none"/>
      </g>
    </defs>

    <!-- background light wedges -->
    <g class="wedges">
      <polygon points="0,0 360,0 0,250" fill="#c8a06a" opacity="0.22"/>
      <polygon points="0,0 240,0 0,140" fill="#d9b478" opacity="0.18"/>
      <polygon points="0,60 330,0 0,420" fill="#a9804f" opacity="0.12"/>
      <polygon points="1200,330 1200,848 640,848" fill="#b88a55" opacity="0.16"/>
      <polygon points="1200,500 1200,848 760,848" fill="#c99a60" opacity="0.18"/>
      <polygon points="1200,600 1200,848 880,848" fill="#d7b98a" opacity="0.2"/>
    </g>

    <!-- frame -->
    <g class="frame" fill="none" stroke="var(--gold)">
      <path stroke-width="5" d="M266 59 H69 V798 H440 M760 798 H1139 V59 H940"/>
      <path stroke-width="2" d="M266 71 H81 V785 H440 M760 785 H1126 V71 H940"/>
    </g>

    <!-- corners -->
    <use href="#corner-ornament"/>
    <use href="#corner-ornament" transform="translate(1200 0) scale(-1 1)"/>
    <use href="#corner-ornament" transform="translate(0 848) scale(1 -1)"/>
    <use href="#corner-ornament" transform="translate(1200 848) scale(-1 -1)"/>

    <!-- rules -->
    <g class="rules" stroke="var(--rule)" stroke-width="1.5" fill="var(--rule)">
      <line x1="290" y1="313" x2="910" y2="313"/>
      <path d="M290 310 l3 3 -3 3 -3 -3z M910 310 l3 3 -3 3 -3 -3z" stroke="none"/>
      <line x1="675" y1="531" x2="934" y2="531"/>
      <path d="M675 528 l3 3 -3 3 -3 -3z M934 528 l3 3 -3 3 -3 -3z" stroke="none"/>
      <line x1="197" y1="707" x2="454" y2="707"/>
      <path d="M197 704 l3 3 -3 3 -3 -3z M454 704 l3 3 -3 3 -3 -3z" stroke="none"/>
      <line x1="757" y1="707" x2="1015" y2="707"/>
      <path d="M757 704 l3 3 -3 3 -3 -3z M1015 704 l3 3 -3 3 -3 -3z" stroke="none"/>
    </g>

    <!-- seal frame -->
    <rect x="545" y="574" width="106" height="181" fill="none" stroke="var(--gold)" stroke-width="1.5"/>
  </svg>

  <h1 class="line display title">Certificate</h1>
  <p class="line display subtitle">Of Completion</p>
  <p class="line caption awarded">This certificate is awarded to</p>
  <p class="line display recipient">John Doe</p>
  <p class="line caption completed">Has successfully completed</p>
  <p class="line display course">Brand Reputation Management<br>Training Course</p>
  <p class="line caption session">Sixteen hours, held on<span class="session__date">NOVEMBER 10, 2019</span></p>

  <p class="caption cert-number">Certificate No.</p>
  <div class="signature" role="img" aria-label="Handwritten signature of the Chief Technology Officer"></div>
  <p class="caption signatory">Chief Technology<br>Officer</p>

  <p class="caption company">BRYNE FJELLVIK</p>
</main>
</body>
</html>
```